Letterhead & Business Card Design Project

Use existing logo to create a new letterhead and business card design. Looking for something clean modern using color options of black, white and gray. The green from the logo may be used lightly as an accent color.

Target Market(s)

Professional business people

Industry/Entity Type

Business

Requirements
Must have
• Business card with front and back design using existing logo.
Nice to have
• Professional presentation
Clean look
Should not have
• No oil rigs, pumpjacks or clip art.

```html
<!DOCTYPE html>
<html lang="en">
<head>
<meta charset="utf-8">
<title>Corvane Exploration Stationery</title>
<link rel="stylesheet" href="https://fonts.googleapis.com/css2?family=EB+Garamond:wght@400&display=swap">
<style>
  :root {
    --backdrop: #e6e4e0;
    --paper: #ffffff;
    --ink: #1a1a1a;
    --gray: #7a7a7a;
    --rule-gray: #9a9a9a;
    --accent: #4caf3f;
  }
  * { box-sizing: border-box; margin: 0; padding: 0; }
  html, body { width: 1200px; height: 1000px; overflow: hidden; }
  body {
    position: relative;
    background: var(--backdrop);
    font-family: "EB Garamond", Georgia, serif;
    color: var(--ink);
  }
  .sheet, .card {
    position: absolute;
    background: var(--paper);
    box-shadow: 0 1px 4px rgba(0,0,0,0.15);
  }
  /* Letterhead */
  .letterhead { left: 65px; top: 24px; width: 643px; height: 964px; }
  .letterhead .brand {
    position: absolute; left: 4px; top: 30px;
    font-size: 30px; letter-spacing: 2px; color: var(--ink);
  }
  .letterhead .address {
    position: absolute; left: 339px; top: 4px;
    font-size: 12.5px; line-height: 17px; letter-spacing: 0.8px; color: var(--gray);
  }
  .letterhead .divider {
    position: absolute; left: 509px; top: 4px; width: 1px; height: 46px;
    background: var(--rule-gray);
  }
  .letterhead .contact {
    position: absolute; left: 530px; top: 17px;
    font-size: 12.5px; line-height: 17px; letter-spacing: 0.8px; color: var(--gray);
  }
  .contact-line { display: flex; align-items: center; gap: 6px; }
  .contact-line svg { width: 11px; height: 11px; fill: var(--ink); }
  .letterhead .footer-rule {
    position: absolute; left: 0; top: 939px; width: 278px; height: 2px;
    background: linear-gradient(90deg, transparent, var(--accent) 20%, var(--accent) 80%, transparent);
  }
  .letterhead .website {
    position: absolute; left: 9px; top: 948px;
    display: flex; align-items: center; gap: 9px;
    font-size: 12.5px; letter-spacing: 1.6px; color: var(--gray);
  }
  .website svg { width: 12px; height: 12px; }
  /* Business cards */
  .card-front { left: 760px; top: 92px; width: 355px; height: 202px; text-align: center; }
  .card-front .person {
    position: absolute; left: 0; right: 0; top: 56px;
    font-size: 22px; letter-spacing: 1px; color: #333;
  }
  .card-front .rule {
    position: absolute; left: 10px; right: 26px; top: 83px; height: 1.5px;
    background: linear-gradient(90deg, transparent, var(--accent) 15%, var(--accent) 85%, transparent);
  }
  .card-front .title {
    position: absolute; left: 0; right: 0; top: 88px;
    font-size: 15px; letter-spacing: 1.2px; color: var(--gray);
  }
  .card-front .cell {
    position: absolute; left: 0; right: 0; top: 106px;
    font-size: 21px; letter-spacing: 1.6px; color: var(--gray);
  }
  .card-back {
    left: 762px; top: 312px; width: 355px; height: 202px;
    display: flex; align-items: center; justify-content: center;
  }
  .card-back .brand { font-size: 30px; letter-spacing: 2px; color: var(--ink); }
</style>
</head>
<body>
  <section class="sheet letterhead">
    <div class="brand">Corvane Exploration</div>
    <address class="address" style="font-style:normal">
      4420 North Ridge Blvd,<br>Suite 210,<br>Tulsa, Oklahoma 74105
    </address>
    <div class="divider"></div>
    <div class="contact">
      <div class="contact-line">
        <svg viewBox="0 0 24 24" aria-hidden="true"><path d="M6.6 10.8a15 15 0 0 0 6.6 6.6l2.2-2.2a1 1 0 0 1 1-.25 11.4 11.4 0 0 0 3.6.57 1 1 0 0 1 1 1V20a1 1 0 0 1-1 1A17 17 0 0 1 3 4a1 1 0 0 1 1-1h3.5a1 1 0 0 1 1 1c0 1.25.2 2.45.57 3.57a1 1 0 0 1-.25 1z"/></svg>
        <span>918.555.0142</span>
      </div>
      <div class="contact-line">
        <svg viewBox="0 0 24 24" aria-hidden="true"><rect x="6" y="2" width="12" height="6"/><rect x="2" y="9" width="20" height="9" rx="1.5"/><rect x="6" y="14" width="12" height="8" fill="#fff" stroke="#1a1a1a" stroke-width="2"/></svg>
        <span>918.555.0143</span>
      </div>
    </div>
    <div class="footer-rule"></div>
    <div class="website">
      <svg viewBox="0 0 24 24" aria-hidden="true"><circle cx="12" cy="12" r="10" fill="#1a1a1a"/><path d="M2 12h20M12 2c3 3 3 17 0 20M12 2c-3 3-3 17 0 20" stroke="#fff" stroke-width="1.5" fill="none"/></svg>
      <span>www.corvaneexploration.com</span>
    </div>
  </section>

  <section class="card card-front">
    <div class="person">MARTIN J HALE</div>
    <div class="rule"></div>
    <div class="title">Managing Member</div>
    <div class="cell">cell 918.555.0197</div>
  </section>

  <section class="card card-back">
    <div class="brand">Corvane Exploration</div>
  </section>
</body>
</html>
```